Window Company website re-design

We are creating a new website design for http://harborpanes.example and we are going to be using wordpress for the site. The idea is to make it appeal to homeowners, more than half of the visitors will be female so the design must appeal to them with appropriate colors and shapes. Historically the website has been dark with a black background and the idea is to keep some of that but make it much brighter with textures and inviting colors.
Major competitors which we will mimic are the following in order of favorites:
http://www.birchvalleyglass.example/ (this is something we really like because of the full width, call to action, easy to navigate, space for
http://www.grainhillexteriors.example/ (this is a nice wide design with a lot of great image space and call to actions)
http://www.restorebyhollister.example/ (the full width is nice here)
http://www.duskpointpanes.example/ (the slide over option showing the window is nice here.)
Others:
http://www.torvane.example/
http://www.quiro.example/home/default.aspx
http://www.hollisterpanes.example/
https://www.glazeplanet.example/
http://www.delcot.example/

Harbor is the leader in the industry so they want a design that is going to portray that. The owners say that their competitors always copy what they do so this design must be cutting edge.

Important elements need to included:
1. Make the design convey very obviously they are a replacement window and door company.
2. Very clear “request a free estimate” call to action box on the homepage.
3. Area for the “Live Support” call to action
4. Navigation:

- Home
- Why Harbor
o Saves Dollars, Makes Sense
o We Have You Covered Start to Finish
o The Harbor Difference
o Pitfalls to Avoid
- Windows and Doors
o Windows
 Double Hung Windows
 Awning Windows
 Basement Hopper Windows
 Bow Windows
 Garden Windows
 Casement Windows
 Bay Windows
 Slider Windows
 Dead-Lite / Specialty / Transom
o Doors
 Storm Doors
 Harbor French Doors
 Patio Slider Doors
 Door Catalog
 Keypad Deadbolt
o Before and After
- About Us
o Testimonials
o Directions
o Warranty
o Employment
o Manufacturing process
o Home Shows
o Community Involvement
- Financing
- Commercial Division
- Careers
- Contact Us

Important elements for the Home Page:
1. Call to action – request a free quote
2. Awards
3. Live support
4. Guarantee
5. Featured testimonials
6. Press releases
7. Locations (Map?)

The attached photos can be used for the homepage images

Target Market(s)

The target market is middle income home owners who want good quality and great service.

Industry/Entity Type

Industry

Font styles to use
Sans Serif

Colors

Designer to choose colors to be used in the design.

Requirements
Must have
• We will need 2 designs, one for the homepage and the other for the inner pages.

2. Awards
3. Live support
4. Guarantee
5. Featured testimonials
6. Press releases
7. Locations (Map?)

```html
<!DOCTYPE html>
<html lang="en">
<head>
<meta charset="utf-8">
<title>Harbor — The Window People</title>
<link href="https://fonts.googleapis.com/css2?family=Open+Sans:wght@400;600;700&display=swap" rel="stylesheet">
<style>
:root{
  --navy:#0f1729;
  --navy-2:#172238;
  --nav-text:#7f95b5;
  --blue:#1f5fa8;
  --blue-bright:#2f8be0;
  --heading:#1d4f8c;
  --text:#6b6b6b;
  --dark:#2a2d32;
  --darker:#1c1e22;
  --white:#ffffff;
  --light:#eeeeee;
}
*{margin:0;padding:0;box-sizing:border-box}
html,body{width:787px;height:1200px;overflow:hidden}
body{font-family:"Open Sans",Arial,sans-serif;color:var(--text);background:var(--white);position:relative}
.abs{position:absolute}
.site-header{position:absolute;left:0;top:0;width:787px;height:50px;background:linear-gradient(#121a2c,var(--navy))}
.brand{left:108px;top:9px;display:flex;align-items:center;gap:6px;color:var(--white);font-weight:700;font-size:20px;line-height:22px}
.brand .mark{width:22px;height:22px;background:var(--white)}
.brand small{display:block;font-size:8px;line-height:10px;font-weight:600;letter-spacing:.3px}
.assist{display:flex;align-items:center;gap:8px;color:var(--white)}
.assist .icon{width:18px;height:18px}
.assist span{display:block;font-size:7.5px;color:#aab3c4}
.assist b{display:block;font-size:11.5px;font-weight:700}
.quote-btn{left:613px;top:14px;width:68px;height:22px;background:linear-gradient(#3a7fd0,#1b58a8);border:1px solid #5e9be0;color:var(--white);text-align:center;font-size:7px;line-height:9px;padding-top:2px}
.quote-btn b{display:block;font-weight:700}
.main-nav{position:absolute;left:0;top:50px;width:787px;height:28px;background:linear-gradient(var(--navy-2),#0c1322);border-top:1px solid #24314c;display:flex;justify-content:center}
.main-nav a{font-size:7.5px;color:var(--nav-text);text-decoration:none;padding:0 15px;line-height:28px;border-right:1px solid #1f2a40}
.main-nav a:last-child{border-right:0}
.hero{position:absolute;left:0;top:78px;width:787px;height:314px;background:linear-gradient(135deg,#a0653d 0%,#b9784a 45%,#8d5a34 70%,#3e5a2a 100%)}
.hero-arrow{top:134px;width:31px;height:31px;background:rgba(0,0,0,.45)}
.hero-caption{left:400px;top:167px;width:315px;height:86px;background:rgba(10,14,24,.88);padding:12px 16px;color:var(--white)}
.hero-caption h1{font-size:14.5px;font-weight:600;line-height:19px}
.hero-caption h1 em{font-style:normal;color:var(--blue-bright)}
.hero-caption p{font-size:7px;line-height:9.5px;margin-top:6px}
.awards{position:absolute;left:0;top:392px;width:787px;height:50px;background:var(--navy)}
.award{display:flex;gap:10px;color:var(--white);top:9px}
.award .badge{width:34px;height:34px;background:#3a4150}
.award .badge.round{border-radius:50%;background:#b9a36a}
.award h3{font-size:7.5px;font-weight:700;margin-top:2px}
.award p{font-size:5.3px;color:#9aa2b3;line-height:7px;margin-top:2px}
.award p i{font-style:italic}
.section-title{font-size:7.5px;font-weight:700;color:var(--heading);letter-spacing:.3px}
.about-text{left:106px;top:477px;width:380px;font-size:6.6px;line-height:12.3px}
.about-text p+p{margin-top:12px}
.why-list{left:498px;top:478px;list-style:none}
.why-list li{display:flex;align-items:center;gap:7px;font-size:6.8px;font-weight:600;color:#4a5670;height:16.8px}
.why-list .dot{width:8px;height:8px}
.guarantee{position:absolute;left:0;top:566px;width:787px;height:135px;background:repeating-linear-gradient(0deg,#24262a 0 2px,#202226 2px 4px)}
.guarantee h2{position:absolute;top:23px;width:787px;text-align:center;font-size:7.3px;font-weight:700;color:var(--blue-bright)}
.guarantee .lead{position:absolute;top:36px;width:787px;text-align:center;font-size:6.6px;color:#8a8d92}
.g-item{top:66px;width:84px}
.g-item .ph{height:36px}
.g-item span{display:block;text-align:center;font-size:5.8px;color:#8a8d92;margin-top:8px;letter-spacing:.3px}
.video{top:741px;width:182px;height:108px;background:#1a1a1a}
.video .ph{height:92px}
.video .bar{height:16px;background:#222;position:relative}
.video .bar i{position:absolute;left:0;top:0;height:3px;width:100%;background:#444}
.video .bar i b{display:block;height:3px;width:20%;background:#b8202a}
.video .bar em{position:absolute;left:45px;top:6px;font-style:normal;font-size:5px;color:var(--white)}
.video .bar svg{position:absolute;left:12px;top:5px}
.update{left:499px;width:190px;display:flex;gap:11px}
.update .thumb{width:46px;height:46px;flex:none}
.update h4{font-size:7.2px;font-weight:600;color:#4a5670}
.update p{font-size:5.3px;line-height:7px;margin-top:5px}
.update a{display:block;text-align:right;font-size:5.3px;font-weight:700;color:var(--heading);text-decoration:none;margin-top:6px}
.newsletter{position:absolute;left:0;top:874px;width:787px;height:44px;background:var(--light);border-top:1px solid #ddd}
.newsletter h3{position:absolute;left:183px;top:11px;font-size:7.8px;font-weight:600;color:var(--heading)}
.newsletter p{position:absolute;left:183px;top:24px;font-size:5.3px;color:#888}
.nl-input{left:360px;top:12px;width:171px;height:19px;background:var(--white);border:1px solid #d5d5d5;font-size:5px;color:#888;padding:6px 8px}
.nl-btn{left:531px;top:12px;width:54px;height:19px;background:linear-gradient(#3b7bc3,#1f5699);color:var(--white);font-size:7px;font-weight:700;text-align:center;line-height:19px}
.site-footer{position:absolute;left:0;top:918px;width:787px;height:247px;background:var(--dark)}
.f-title{font-size:7.3px;font-weight:700;color:var(--white);line-height:10px}
.f-rule{height:1px;background:#3c4047}
.f-text{font-size:5.8px;line-height:9px;color:#d7d9dc}
.f-list{list-style:none}
.f-list li{font-size:5.3px;line-height:8px;color:#d7d9dc;height:11.8px}
.f-list li::before{content:"›";margin-right:5px;color:#999}
.contact-row{display:flex;align-items:center;gap:11px;font-size:5.3px;color:#d7d9dc;height:14.8px}
.contact-row svg{flex:none;width:9px}
.field{background:var(--white);border:1px solid #ccc;font-size:5px;color:#888;padding:4px 5px}
.send{left:627px;top:164px;width:54px;height:18px;background:linear-gradient(#4b5566,#353c48);border:1px solid #5a6474;color:var(--white);font-size:5.8px;font-weight:700;text-align:center;line-height:16px}
.social{display:flex;gap:8px}
.social i{width:16px;height:16px;border-radius:50%;background:var(--white);display:block}
.footer-bottom{position:absolute;left:0;top:1165px;width:787px;height:35px;background:var(--darker);font-size:5.3px;color:#7b7e83}
</style>
</head>
<body>

<header class="site-header">
  <div class="abs brand"><span class="mark"></span><div>Harbor<small>“The Window People”</small></div></div>
  <div class="abs assist" style="left:373px;top:14px">
    <svg class="icon" viewBox="0 0 18 18"><rect x="1" y="1" width="16" height="16" fill="none" stroke="#c8ccd4" stroke-width="1.5"/><circle cx="9" cy="7" r="3" fill="#c8ccd4"/><path d="M3.5 16c1-3.5 3-5 5.5-5s4.5 1.5 5.5 5z" fill="#c8ccd4"/></svg>
    <div><span>Need Assistance?</span><b>Live Support</b></div>
  </div>
  <div class="abs assist" style="left:486px;top:14px">
    <svg class="icon" viewBox="0 0 18 18"><rect x="1" y="1" width="16" height="16" rx="2" fill="none" stroke="#c8ccd4" stroke-width="1.5"/><path d="M6 4.5l2 2-1 1.5c.7 1.5 1.5 2.3 3 3l1.5-1 2 2-1.5 1.5c-3.5 0-7.5-4-7.5-7.5z" fill="#c8ccd4"/></svg>
    <div><span>Call us today</span><b>(800) 555-0147</b></div>
  </div>
  <div class="abs quote-btn">Request<b>FREE QUOTE</b></div>
</header>

<nav class="main-nav">
  <a href="#" aria-label="Home"><svg width="8" height="7" viewBox="0 0 8 7"><path d="M4 0l4 3.5H7V7H5V5H3v2H1V3.5H0z" fill="#c8ccd4"/></svg></a>
  <a href="#">Why Choose Harbor</a><a href="#">Windows and Doors</a><a href="#">About Us</a><a href="#">Financing</a><a href="#">Commercial Division</a><a href="#">Careers</a><a href="#">Contact Us</a>
</nav>

<section class="hero" role="img" aria-label="Brick house with a wide white replacement window, flower box and arched entry">
  <div class="abs hero-arrow" style="left:0"><svg width="31" height="31"><path d="M18 10l-5 5.5 5 5.5" stroke="#fff" stroke-width="1.6" fill="none"/></svg></div>
  <div class="abs hero-arrow" style="right:0"><svg width="31" height="31"><path d="M13 10l5 5.5-5 5.5" stroke="#fff" stroke-width="1.6" fill="none"/></svg></div>
  <div class="abs hero-caption">
    <h1>Replacing your home's windows with <em>high-performance.</em></h1>
    <p>For over 30 years we have been designing windows to fit your world, Harbor Windows is one of the wisest home improvement investments you'll ever make.</p>
  </div>
</section>

<section class="awards">
  <div class="abs award" style="left:156px"><div class="badge" role="img" aria-label="Award trophy"></div>
    <div><h3>TOP COMPANY IN THE COUNTRY</h3><p>in the window category for three consecutive years.</p><p><i>-Home Renovator Quarterly, most popular trade magazines</i></p></div></div>
  <div class="abs award" style="left:405px"><div class="badge round" role="img" aria-label="2012 award seal"></div>
    <div><h3>BEST INTERNET SITE FOR A PRODUCT SUPPLIER</h3><p><i>—by the Regional Home Builders Guild<br>of New Jersey for 2012</i></p></div></div>
</section>

<h2 class="abs section-title" style="left:106px;top:459px">ABOUT OUR COMPANY</h2>
<div class="abs about-text">
  <p>We offer a wide selection of top quality, custom-made windows to fit your home because we know you appreciate variety, expect quality and demand affordability.</p>
  <p>Our windows are a reflection of our dedication and commitment to excellence. The skill and care our people take in manufacturing quality replacement windows originates from the tremendous pride we exhibit in all phases of production, including precise engineering and thorough quality control testing. All windows are made in the USA.</p>
</div>
<h2 class="abs section-title" style="left:500px;top:459px">WHY CHOOSE US?</h2>
<ul class="abs why-list">
  <li><svg class="dot" viewBox="0 0 8 8"><circle cx="4" cy="4" r="4" fill="#1d3a66"/><path d="M3.2 2.3L5 4 3.2 5.7" stroke="#fff" fill="none"/></svg>Save dollars, make sense</li>
  <li><svg class="dot" viewBox="0 0 8 8"><circle cx="4" cy="4" r="4" fill="#1d3a66"/><path d="M3.2 2.3L5 4 3.2 5.7" stroke="#fff" fill="none"/></svg>We cover start to finish</li>
  <li><svg class="dot" viewBox="0 0 8 8"><circle cx="4" cy="4" r="4" fill="#1d3a66"/><path d="M3.2 2.3L5 4 3.2 5.7" stroke="#fff" fill="none"/></svg>Award winning services</li>
  <li><svg class="dot" viewBox="0 0 8 8"><circle cx="4" cy="4" r="4" fill="#1d3a66"/><path d="M3.2 2.3L5 4 3.2 5.7" stroke="#fff" fill="none"/></svg>We guarantee 100% satisfaction</li>
</ul>

<section class="guarantee">
  <h2>OUR GUARANTEE: WE COVER EVERYTHING 100%.</h2>
  <p class="lead">We are so confident in our work that we offer one of the best guarantees in the industry. We even cover labor and installation.</p>
  <div class="abs g-item" style="left:106px"><div class="ph" role="img" aria-label="House roofline with windows" style="background:linear-gradient(#7a2a22,#d8d6d2)"></div><span>WINDOWS</span></div>
  <div class="abs g-item" style="left:204px"><div class="ph" role="img" aria-label="Broken window glass" style="background:linear-gradient(135deg,#9fb2c0,#3c4852)"></div><span>GLASS BREAKAGE</span></div>
  <div class="abs g-item" style="left:303px"><div class="ph" role="img" aria-label="Window seal close-up" style="background:linear-gradient(#e4ecf0,#9fc8e2)"></div><span>SEALS</span></div>
  <div class="abs g-item" style="left:401px"><div class="ph" role="img" aria-label="Vinyl sign with store hours" style="background:linear-gradient(#6a6258,#3a352f)"></div><span>VINYL</span></div>
  <div class="abs g-item" style="left:499px"><div class="ph" role="img" aria-label="Window hardware parts" style="background:linear-gradient(135deg,#d8d4c8,#8f8a7f)"></div><span>PARTS</span></div>
  <div class="abs g-item" style="left:597px"><div class="ph" role="img" aria-label="Hard hat and blueprints" style="background:linear-gradient(135deg,#e8b21c,#9ab6d0)"></div><span>SERVICE</span></div>
</section>

<h2 class="abs section-title" style="left:105px;top:720px">WHAT OUR CLIENTS SAY ABOUT US</h2>
<div class="abs video" style="left:106px"><div class="ph" role="img" aria-label="Video testimonial from a male customer" style="background:linear-gradient(#5a5550,#2a2c33)"></div>
  <div class="bar"><i><b></b></i><svg width="24" height="7"><path d="M0 0l6 3.5L0 7z" fill="#bbb"/><path d="M14 2h2l3-2v7l-3-2h-2z" fill="#bbb"/></svg><em>0:02 / 4:17</em></div></div>
<div class="abs video" style="left:303px"><div class="ph" role="img" aria-label="Video testimonial from a female customer" style="background:linear-gradient(#8a7f70,#3a3430)"></div>
  <div class="bar"><i><b></b></i><svg width="24" height="7"><path d="M0 0l6 3.5L0 7z" fill="#bbb"/><path d="M14 2h2l3-2v7l-3-2h-2z" fill="#bbb"/></svg><em>0:02 / 4:17</em></div></div>

<h2 class="abs section-title" style="left:499px;top:720px">LATEST UPDATES</h2>
<div class="abs update" style="top:740px"><div class="thumb" role="img" aria-label="Newspaper clipping award" style="background:linear-gradient(#f1ead4,#d9cfae);border:1px solid #ccc"></div>
  <div><h4>Irraer sit voluptatem accusantium</h4><p>Proin gravida nibh vel velit auctor aliquet. Aenean sollicitudin, lorem quis bibendum auctor, nisi elit consequat ipsum, nec sagittis sem nibh id elit.</p><a href="#">Continue reading...</a></div></div>
<div class="abs update" style="top:802px"><div class="thumb" role="img" aria-label="Suburban house exterior" style="background:linear-gradient(#9ec0dc,#b48a66 60%,#5d7a3e)"></div>
  <div><h4>Irraer sit voluptatem accusantium</h4><p>Proin gravida nibh vel velit auctor aliquet. Aenean sollicitudin, lorem quis bibendum auctor, nisi elit consequat ipsum, nec sagittis sem nibh id elit.</p><a href="#">Continue reading...</a></div></div>

<section class="newsletter">
  <h3>Subscribe to our Newsletter</h3>
  <p>Sign up and stay updated. Get the latest new and special offers.</p>
  <div class="abs nl-input">Enter Your Email Address</div>
  <div class="abs nl-btn">Submit</div>
</section>

<footer class="site-footer">
  <div class="abs" style="left:107px;top:37px;width:104px"><div class="f-title">About Us</div><div class="f-rule" style="margin-top:5px"></div></div>
  <div class="abs brand" style="top:78px;left:108px"><span class="mark"></span><div>Harbor<small>“The Window People”</small></div></div>
  <p class="abs f-text" style="left:106px;top:117px;width:104px">Vestibulum id ligula porta felis euismod semper. Integer posuere erat a ante.</p>

  <div class="abs" style="left:254px;top:37px;width:106px"><div class="f-title">Contact Details</div><div class="f-rule" style="margin-top:5px"></div></div>
  <p class="abs f-text" style="left:254px;top:56px;width:106px">There are many variations of passages of Lorem Ipsum available, but the majority have suffered alteration.</p>
  <div class="abs" style="left:253px;top:103px">
    <div class="contact-row"><svg height="9" viewBox="0 0 7 9"><path d="M3.5 0a3.5 3.5 0 013.5 3.5C7 6 3.5 9 3.5 9S0 6 0 3.5A3.5 3.5 0 013.5 0z" fill="#888"/><circle cx="3.5" cy="3.5" r="1.3" fill="#2a2d32"/></svg>Harborview, NJ</div>
    <div class="contact-row"><svg height="7" viewBox="0 0 9 7"><rect width="9" height="7" fill="#888"/><path d="M0 0l4.5 4L9 0" stroke="#2a2d32" fill="none"/></svg>info@harborpanes.example</div>
    <div class="contact-row"><svg height="8" viewBox="0 0 8 8"><path d="M1 0l2 2-1 1.5c.6 1.2 1.3 1.9 2.5 2.5L6 5l2 2-1.2 1C3.5 8 0 4.5 0 1.2z" fill="#888"/></svg>800-555-0193</div>
  </div>

  <div class="abs f-title" style="left:105px;top:168px">Navigation</div>
  <ul class="abs f-list" style="left:106px;top:184px"><li>Home</li><li>About</li><li>Services</li><li>Contact</li></ul>
  <div class="abs f-title" style="left:252px;top:168px">Services</div>
  <ul class="abs f-list" style="left:253px;top:184px"><li>Menu1</li><li>Menu1</li><li>Menu1</li><li>Menu1</li></ul>

  <div class="abs" style="left:399px;top:0;width:1px;height:247px;background:#33363c"></div>
  <div class="abs f-title" style="left:436px;top:37px">We'd love to hear from you.</div>
  <p class="abs f-text" style="left:436px;top:55px;width:250px">If you you have questions or inquires, please don't hesitate to contact us through phone or you can send your message using the contact form below:</p>
  <div class="abs field" style="left:436px;top:82px;width:113px;height:17px">Name</div>
  <div class="abs field" style="left:436px;top:104px;width:113px;height:17px">Email</div>
  <div class="abs field" style="left:436px;top:127px;width:113px;height:17px">Phone</div>
  <div class="abs field" style="left:559px;top:82px;width:123px;height:62px">Message</div>
  <div class="abs send">Send Email</div>
  <div class="abs f-title" style="left:435px;top:194px">Social Links</div>
  <div class="abs social" style="left:435px;top:206px"><i aria-label="Social link"></i><i aria-label="Social link"></i><i aria-label="Social link"></i><i aria-label="Social link"></i></div>
</footer>

<div class="footer-bottom">
  <span class="abs" style="left:106px;top:14px">Copyright 2014 © Harbor - All Rights Reserved</span>
  <span class="abs" style="left:560px;top:14px">Site Map &nbsp;•&nbsp; Privacy Policy &nbsp;•&nbsp; Disclaimer</span>
</div>

</body>
</html>
```